International Clinical Software Company needs a new business card design

We are looking for a new business card design for our company that has recently expanded into the UK market, making us a multinational company.
After having rebranded our website and produced a new style guide, we are looking for a business card that is creative and attention grabbing, while being consistent with the style and colour scheme used on the new website, www.brookvale.example
We produce care management technology for the aged care market, but the main aspect we aim to communicate is the human element of our software, and the way it assists in providing better care for aged people, and stronger relationships between aged people and the staff that care for them.
Our current business card is a dark green with gold text, which makes the text quite difficult to read, not very aesthetically appealing and the colour scheme looks quite dated.
We would like something fresh and modern, that can still be colourful but doesn't use large blocks of dark colour, and uses the colours within our logo.
Something tying in with the leaves that are used in our logo could work quite nicely, along with the Autumn/Fall colours of soft greens, yellows and reds (also in our existing logo). However also happy to look at fresh, completely out of the box ideas we may not have yet considered.
Target Market(s)
The people that receive this business card work in the aged card or health industry and are either corporate/management level staff or clinical (Registered Nurses, care workers etc.)
Industry/Entity Type
Health Product
Contact Information for Business Card
Company Name - BrookvaleTech
Company locations: United Kingdom, Australia, New Zealand
Staff Details:
Staff name: Dermot Quill
Staff job title: Executive Chairman
Staff email: d.quill@brookvale.example
Office phone number: 01632 960418
Font styles to use
Other font styles liked:
- Calibri
Requirements
Must have
- Must include the BrookvaleTech brand name in it's current font
- Must include logo (3 leaves in gold circle)
- Must include Business Card Details
Nice to have
- Elements of gold
- White space
- Something autumn themed but not too cliched
Should not have
- No blue - used by a major competitor and we would like to differentiate from them
- Large blocks of dark green colour (the green that appears in our leaves on the logo on our current business card is the background colour and it is far too dark)

```html
<!DOCTYPE html>
<html lang="en">
<head>
<meta charset="utf-8">
<title>BrookvaleTech Business Card</title>
<link rel="stylesheet" href="https://fonts.googleapis.com/css2?family=Carlito:wght@400;700&display=swap">
<style>
  :root {
    --page-bg: #e4e4e4;
    --card-bg: #f5f5f4;
    --brand-gold: #9c9070;
    --text-dark: #636363;
    --text-mid: #707070;
    --accent-red: #9b1d4f;
    --accent-yellow: #c9b92f;
    --accent-green: #5b8a2b;
    --wash-a: rgba(214, 206, 170, 0.28);
    --wash-b: rgba(226, 190, 196, 0.22);
  }
  html, body {
    margin: 0;
    padding: 0;
    width: 1105px;
    height: 1200px;
    overflow: hidden;
    background: var(--page-bg);
    font-family: "Carlito", "Calibri", sans-serif;
  }
  .business-card {
    position: absolute;
    left: 52px;
    top: 315px;
    width: 1000px;
    height: 569px;
    background: var(--card-bg);
    overflow: hidden;
  }
  .leaf-wash {
    position: absolute;
    left: 0;
    top: 0;
    width: 360px;
    height: 569px;
    background: linear-gradient(160deg, var(--wash-a) 0%, rgba(255,255,255,0) 45%, var(--wash-b) 85%, rgba(255,255,255,0) 100%);
  }
  .brand {
    position: absolute;
    top: 56px;
    right: 61px;
    display: flex;
    align-items: center;
    gap: 18px;
  }
  .brand-dot {
    width: 132px;
    height: 132px;
    border-radius: 50%;
    background: var(--brand-gold);
  }
  .brand-name {
    font-size: 44px;
    font-weight: 400;
    color: var(--brand-gold);
    letter-spacing: 0.5px;
  }
  .staff-name {
    position: absolute;
    left: 50px;
    top: 305px;
    margin: 0;
    font-size: 36px;
    font-weight: 700;
    color: var(--text-dark);
  }
  .staff-title {
    position: absolute;
    left: 50px;
    top: 352px;
    margin: 0;
    font-size: 27px;
    color: var(--text-mid);
  }
  .accent-rule {
    position: absolute;
    top: 368px;
    left: 314px;
    width: 625px;
    height: 3px;
    display: flex;
    gap: 5px;
  }
  .accent-rule span { flex: 1; }
  .accent-rule .red { background: var(--accent-red); }
  .accent-rule .yellow { background: var(--accent-yellow); }
  .accent-rule .green { background: var(--accent-green); }
  .contact-list, .location-list {
    position: absolute;
    top: 410px;
    margin: 0;
    padding: 0;
    list-style: none;
    font-size: 27px;
    line-height: 39px;
    color: var(--text-mid);
  }
  .contact-list { left: 50px; }
  .contact-list li { display: flex; align-items: center; gap: 14px; }
  .contact-list svg { width: 24px; height: 24px; fill: var(--text-mid); }
  .location-list { right: 61px; text-align: right; }
</style>
</head>
<body>
  <main class="business-card">
    <div class="leaf-wash" role="img" aria-label="Faint soft leaf shapes in pale gold and rose"></div>

    <div class="brand">
      <div class="brand-dot"></div>
      <span class="brand-name">BrookvaleTech</span>
    </div>

    <h1 class="staff-name">Dermot Quill</h1>
    <p class="staff-title">Executive Chairman</p>

    <div class="accent-rule" aria-hidden="true">
      <span class="red"></span><span class="yellow"></span><span class="green"></span>
    </div>

    <ul class="contact-list">
      <li>
        <svg viewBox="0 0 24 24" aria-hidden="true"><path d="M6.6 10.8c1.4 2.8 3.8 5.1 6.6 6.6l2.2-2.2c.3-.3.7-.4 1-.2 1.1.4 2.3.6 3.6.6.6 0 1 .4 1 1V20c0 .6-.4 1-1 1C10.6 21 3 13.4 3 4c0-.6.4-1 1-1h3.5c.6 0 1 .4 1 1 0 1.3.2 2.5.6 3.6.1.3 0 .7-.2 1L6.6 10.8z"/></svg>
        01632 960418
      </li>
      <li>
        <svg viewBox="0 0 24 24" aria-hidden="true"><path d="M2 5h20v2l-10 6L2 7V5zm0 4.3l10 6 10-6V19H2V9.3z"/></svg>
        d.quill@brookvale.example
      </li>
      <li>
        <svg viewBox="0 0 24 24" aria-hidden="true"><path d="M12 2a10 10 0 1 0 0 20 10 10 0 0 0 0-20zm-1 17.9A8 8 0 0 1 4.2 10.5L9 15.3v1a2 2 0 0 0 2 2v1.6zm6.9-2.5A2 2 0 0 0 16 16h-1v-3a1 1 0 0 0-1-1H8v-2h2a1 1 0 0 0 1-1V7h2a2 2 0 0 0 2-2v-.4a8 8 0 0 1 2.9 12.8z"/></svg>
        www.brookvale.example
      </li>
    </ul>

    <ul class="location-list">
      <li>United Kingdom</li>
      <li>Australia</li>
      <li>New Zealand</li>
    </ul>
  </main>
</body>
</html>
```